Stationary design for real estate company in Trinidad and Tobago

Kestra Realty Ltd. , real estate company operating in Trinidad and Tobago, requires a sleek, modern and professional stationary package to wow our customers and potential new clients. we want to look sleek and professional; first impressions count in this business!
Business Address:
Level 1, Marlowe Point Tower
4C Seldon Grove Boulevard
Marlowe Point
Colwyn Pereira Highway
Port of Spain
Trinidad
Tel: + 1 868 555 0147
www.kestra-tt.com
info@kestra-tt.com

```html
<!DOCTYPE html>
<html lang="en">
<head>
<meta charset="utf-8">
<title>Kestra Realty Stationery</title>
<link rel="stylesheet" href="https://fonts.googleapis.com/css2?family=Lato:wght@400;700&display=swap">
<style>
:root{
  --navy:#1d3461;
  --gold:#c49a56;
  --gold-light:#e8d5b0;
  --ink:#4a4a4a;
  --white:#ffffff;
  --header-bg:#ececec;
  --stage-bg:#2e2f31;
  --sheet-bg:#dcdcdc;
}
*{box-sizing:border-box;margin:0;padding:0}
html,body{width:1200px;height:2366px;overflow:hidden}
body{position:relative;font-family:'Lato',sans-serif;color:var(--ink);background:var(--sheet-bg)}
.abs{position:absolute}

/* brand lockup */
.brand{display:flex;align-items:center;gap:.3em;color:var(--navy);font-weight:400;line-height:1;white-space:nowrap}
.brand-dot{width:.7em;height:.7em;border-radius:50%;background:var(--gold);flex:none}
.brand-text{display:flex;flex-direction:column;align-items:center}
.brand-name{letter-spacing:.03em}
.brand-sub{font-size:.26em;letter-spacing:1.5em;margin-top:.35em;padding-left:1.5em}
.brand.on-dark{color:var(--white)}

/* bottom stripe */
.stripe{position:absolute;left:0;right:0;bottom:14px;height:5px}
.stripe .gold-line{position:absolute;left:0;bottom:0;height:2px;width:60%;background:linear-gradient(90deg,var(--gold-light),var(--gold))}
.stripe .navy-line{position:absolute;right:0;bottom:0;height:5px;width:40%;background:var(--navy)}
.stripe.on-dark .white-line{position:absolute;left:0;bottom:0;height:3px;width:50%;background:var(--white)}
.stripe.on-dark .gold-fade{position:absolute;left:50%;bottom:0;height:2px;width:50%;background:linear-gradient(90deg,var(--gold),rgba(196,154,86,0))}

/* sections */
.page-header{left:0;top:0;width:1200px;height:104px;background:var(--header-bg);display:flex;align-items:center;justify-content:center}
.stage{left:0;top:104px;width:1200px;height:870px;background:var(--stage-bg)}
.piece{position:absolute;background:var(--white);box-shadow:0 3px 8px rgba(0,0,0,.18);overflow:hidden}
.piece.navy{background:var(--navy)}

.person-name{color:var(--gold);font-weight:700;letter-spacing:.02em;white-space:nowrap}
.person-name b{color:var(--navy)}
.role{color:var(--ink)}
.contact{display:flex;align-items:center;gap:5px;white-space:nowrap}
.icon{display:inline-block;background:var(--navy);border-radius:2px;flex:none}
.address{color:var(--ink);line-height:1.3;white-space:nowrap}
</style>
</head>
<body>

<header class="page-header abs">
  <div class="brand" style="font-size:40px">
    <span class="brand-dot"></span>
    <span class="brand-text"><span class="brand-name">KESTRA</span><span class="brand-sub">REALTY</span></span>
  </div>
</header>

<section class="stage abs">
  <div class="piece navy" style="left:620px;top:250px;width:480px;height:287px">
    <div class="brand on-dark abs" style="font-size:56px;left:110px;top:100px">
      <span class="brand-dot"></span>
      <span class="brand-text"><span class="brand-name">KESTRA</span><span class="brand-sub">REALTY</span></span>
    </div>
    <div class="stripe on-dark" style="bottom:26px"><span class="white-line"></span><span class="gold-fade"></span></div>
  </div>
  <div class="piece" style="left:100px;top:330px;width:480px;height:287px">
    <div class="brand abs" style="font-size:36px;left:26px;top:108px">
      <span class="brand-dot"></span>
      <span class="brand-text"><span class="brand-name">KESTRA</span><span class="brand-sub">REALTY</span></span>
    </div>
    <div class="abs" style="left:240px;top:60px;font-size:11px">
      <div class="person-name" style="font-size:17px">DANIEL R. <b>OKAFOR</b></div>
      <div class="role" style="margin:2px 0 12px">Managing Director</div>
      <div class="contact"><span class="icon" style="width:11px;height:11px"></span>+ 1 868 555 0147</div>
      <div class="contact" style="margin:4px 0 12px"><span class="icon" style="width:11px;height:11px"></span>info@kestra-tt.com</div>
      <div class="address">Level 1, Marlowe Point Tower<br>4C Seldon Grove Boulevard Marlowe Point</div>
      <div class="address" style="margin-top:8px">Colwyn Pereira Highway<br>Port of Spain, Trinidad</div>
    </div>
    <div class="stripe" style="bottom:26px"><span class="gold-line"></span><span class="navy-line"></span></div>
  </div>
</section>

<!-- business card front -->
<div class="piece navy" style="left:49px;top:1020px;width:264px;height:159px">
  <div class="brand on-dark abs" style="font-size:28px;left:66px;top:58px">
    <span class="brand-dot"></span>
    <span class="brand-text"><span class="brand-name">KESTRA</span><span class="brand-sub">REALTY</span></span>
  </div>
  <div class="stripe on-dark" style="bottom:20px"><span class="white-line"></span><span class="gold-fade"></span></div>
</div>

<!-- business card back -->
<div class="piece" style="left:351px;top:1020px;width:265px;height:159px">
  <div class="brand abs" style="font-size:18px;left:18px;top:66px">
    <span class="brand-dot"></span>
    <span class="brand-text"><span class="brand-name">KESTRA</span><span class="brand-sub">REALTY</span></span>
  </div>
  <div class="abs" style="left:137px;top:30px;font-size:6px">
    <div class="person-name" style="font-size:9px">DANIEL R. <b>OKAFOR</b></div>
    <div class="role" style="margin:1px 0 5px">Managing Director</div>
    <div class="contact"><span class="icon" style="width:7px;height:7px"></span>+ 1 868 555 0147</div>
    <div class="contact" style="margin:3px 0 6px"><span class="icon" style="width:7px;height:7px"></span>info@kestra-tt.com</div>
    <div class="address">Level 1, Marlowe Point Tower<br>4C Seldon Grove Boulevard Marlowe Point</div>
    <div class="address" style="margin-top:5px">Colwyn Pereira Highway<br>Port of Spain, Trinidad</div>
  </div>
  <div class="stripe" style="bottom:18px"><span class="gold-line"></span><span class="navy-line"></span></div>
</div>

<!-- letterhead -->
<div class="piece" style="left:652px;top:1022px;width:482px;height:675px">
  <div class="brand abs" style="font-size:26px;left:18px;top:20px">
    <span class="brand-dot"></span>
    <span class="brand-text"><span class="brand-name">KESTRA</span><span class="brand-sub">REALTY</span></span>
  </div>
  <div class="abs" style="right:14px;top:14px;font-size:8px;text-align:right;line-height:15px">
    <div class="contact" style="justify-content:flex-end">+ 1 868 555 0147<span class="icon" style="width:9px;height:9px"></span></div>
    <div class="contact" style="justify-content:flex-end">info@kestra-tt.com<span class="icon" style="width:9px;height:9px"></span></div>
    <div class="contact" style="justify-content:flex-end">www.kestra-tt.com<span class="icon" style="width:9px;height:9px"></span></div>
  </div>
  <div class="address abs" style="left:15px;bottom:28px;font-size:7.5px">Level 1, Marlowe Point Tower<br>4C Seldon Grove Boulevard, Marlowe Point</div>
  <div class="address abs" style="left:179px;bottom:28px;font-size:7.5px">Colwyn Pereira Highway<br>Port of Spain, Trinidad</div>
  <div class="stripe" style="bottom:17px"><span class="gold-line"></span><span class="navy-line"></span></div>
</div>

<!-- compliment slip -->
<div class="piece" style="left:49px;top:1221px;width:568px;height:144px">
  <div class="brand abs" style="font-size:22px;left:18px;top:56px">
    <span class="brand-dot"></span>
    <span class="brand-text"><span class="brand-name">KESTRA</span><span class="brand-sub">REALTY</span></span>
  </div>
  <div class="abs" style="left:142px;top:30px;font-size:8px">
    <div class="person-name" style="font-size:11px">DANIEL R. <b>OKAFOR</b></div>
    <div class="role" style="margin:2px 0 9px">Managing Director</div>
    <div class="contact"><span class="icon" style="width:9px;height:9px"></span>+ 1 868 555 0147</div>
    <div class="contact" style="margin:6px 0"><span class="icon" style="width:9px;height:9px"></span>info@kestra-tt.com</div>
    <div class="contact"><span class="icon" style="width:9px;height:9px"></span>www.kestra-tt.com</div>
  </div>
  <div class="abs" style="left:241px;top:66px;font-size:8px">
    <div class="address">Level 1, Marlowe Point Tower<br>4C Seldon Grove Boulevard, Marlowe Point</div>
    <div class="address" style="margin-top:8px">Colwyn Pereira Highway<br>Port of Spain, Trinidad</div>
  </div>
  <div class="stripe" style="bottom:10px"><span class="gold-line"></span><span class="navy-line"></span></div>
</div>

<!-- envelope -->
<div class="piece" style="left:49px;top:1413px;width:567px;height:285px">
  <div class="brand abs" style="font-size:28px;left:18px;top:20px">
    <span class="brand-dot"></span>
    <span class="brand-text"><span class="brand-name">KESTRA</span><span class="brand-sub">REALTY</span></span>
  </div>
  <div class="address abs" style="left:18px;bottom:28px;font-size:7.5px">Level 1, Marlowe Point Tower<br>4C Seldon Grove Boulevard, Marlowe Point</div>
  <div class="address abs" style="left:206px;bottom:28px;font-size:7.5px">Colwyn Pereira Highway<br>Port of Spain, Trinidad</div>
  <div class="stripe" style="bottom:17px"><span class="gold-line"></span><span class="navy-line"></span></div>
</div>

<!-- presentation folder -->
<div class="abs" style="left:48px;top:1742px;width:682px;height:560px">
  <svg class="abs" width="682" height="560" viewBox="0 0 682 560" aria-hidden="true">
    <polygon points="0,315 26,306 26,436 0,426" fill="var(--navy)"/>
    <polygon points="656,306 682,315 682,426 656,436" fill="var(--navy)"/>
    <rect x="26" y="0" width="314" height="560" fill="var(--navy)"/>
    <rect x="340" y="0" width="316" height="412" fill="var(--white)"/>
    <polygon points="340,412 656,412 656,560 360,560" fill="var(--navy)"/>
    <rect x="26" y="385" width="115" height="3" fill="var(--white)"/>
    <rect x="141" y="385" width="199" height="2" fill="var(--gold)" opacity=".7"/>
    <rect x="340" y="385" width="196" height="2" fill="var(--gold)"/>
    <rect x="536" y="384" width="120" height="4" fill="var(--navy)"/>
  </svg>
  <div class="abs" style="left:127px;top:138px;font-size:10.5px;color:var(--white);line-height:1.3">
    <div class="contact"><span class="icon" style="width:12px;height:12px;background:var(--gold)"></span>+ 1 868 555 0147</div>
    <div class="contact" style="margin:8px 0"><span class="icon" style="width:12px;height:12px;background:var(--gold)"></span>info@kestra-tt.com</div>
    <div class="contact"><span class="icon" style="width:12px;height:12px;background:var(--gold)"></span>www.kestra-tt.com</div>
    <div style="margin-top:14px;font-size:9px">Level 1, Marlowe Point Tower<br>4C Seldon Grove Boulevard<br>Marlowe Point</div>
    <div style="margin-top:10px;font-size:9px">Colwyn Pereira Highway<br>Port of Spain, Trinidad</div>
  </div>
  <div class="brand abs" style="font-size:50px;left:376px;top:192px">
    <span class="brand-dot"></span>
    <span class="brand-text"><span class="brand-name">KESTRA</span><span class="brand-sub">REALTY</span></span>
  </div>
</div>

<!-- apparel print -->
<div class="piece" style="left:752px;top:1792px;width:370px;height:460px">
  <div class="brand abs" style="font-size:32px;left:88px;top:200px">
    <span class="brand-dot"></span>
    <span class="brand-text"><span class="brand-name">KESTRA</span><span class="brand-sub">REALTY</span></span>
  </div>
</div>

</body>
</html>
```